Lantern Jubilee Flyer

I need an 8.5x11 or 8.5x14 or 11x17 flyer for a benefit concert. Logo has already been designed; uploading several different versions, and you could choose which you want to use. For flyer design: something subtly musical (not a big fan of using musical symbols in the design, treble clefs, eighth notes, etc.) But something classy. I'm uploading unformatted copy, and two logos: one of the radio station that is helping to sponsor the event, and one for the organization the concert is benefitting. This is quick turnaround, so I promise to be very responsive with feedback. Thanks!

```html
<!DOCTYPE html>
<html lang="en">
<head>
<meta charset="utf-8">
<title>Lantern Jubilee – Live Music Flyer</title>
<link rel="stylesheet" href="https://fonts.googleapis.com/css2?family=Alfa+Slab+One&family=Oswald:wght@400;500;700&display=swap">
<style>
  :root{
    --stage:#e4e4e4;
    --paper:#e6d8b8;
    --paper-edge:#c4a878;
    --gold-light:#eaa63a;
    --gold-dark:#b06a18;
    --stripe:#b3231c;
    --band-blue:#2f5fc4;
    --band-glow:#8fc8ff;
    --band-dark:#0a1230;
    --drum-red:#cf2420;
    --drum-glow:#ef5a48;
    --drum-dark:#6e0c0a;
    --crowd-glow:#ffe2c8;
    --crowd-mid:#d8402a;
    --crowd-dark:#160604;
    --ink:#1d1b18;
    --brown:#9a4a1e;
    --red-text:#d0281e;
    --violet:#7a3c9e;
    --date-red:#8e1a16;
    --night:#1f1c1a;
    --lime:#b9d532;
    --yellow:#f6e21a;
    --orange:#e8741c;
    --white:#ffffff;
  }
  *{margin:0;padding:0;box-sizing:border-box}
  html,body{width:707px;height:1200px;overflow:hidden;background:var(--stage)}
  .flyer-frame{position:absolute;left:0;top:143px;width:707px;height:913px;overflow:hidden}
  .flyer{
    position:absolute;left:0;top:0;width:515px;height:665px;
    transform:scale(1.3728);transform-origin:0 0;
    background:radial-gradient(ellipse at 60% 45%,var(--paper) 40%,var(--paper-edge) 100%);
    overflow:hidden;font-family:"Oswald",sans-serif;color:var(--ink);
  }
  .layer{position:absolute;left:0;top:0;width:515px;height:665px}
  .rot{position:absolute;left:var(--x);top:var(--y);transform:translate(-50%,-50%) rotate(var(--a));white-space:nowrap}

  .station{font-weight:700;font-size:26px;color:var(--orange);letter-spacing:.5px;display:flex;align-items:center;gap:6px}
  .station .mark{width:14px;height:14px;background:var(--orange)}

  .event-name{display:flex;align-items:center;gap:7px;font-weight:700;color:var(--violet);line-height:.95;font-size:23px;text-transform:uppercase}
  .event-name .mark{width:16px;height:16px;background:var(--violet);flex:none}

  .date-badge{width:56px;height:60px;background:var(--date-red);border-radius:7px;color:var(--white);
    display:flex;flex-direction:column;align-items:center;justify-content:center;line-height:1;font-weight:700;
    box-shadow:1px 2px 3px rgba(0,0,0,.35)}
  .date-badge .day{font-size:22px}
  .date-badge .month{font-size:12px}
  .date-badge .year{font-size:12px;font-weight:500}

  .venue-box{width:175px;height:82px;background:var(--night);border-radius:12px;color:var(--lime);
    padding:8px 0 0 24px;line-height:1;font-weight:700}
  .venue-box .lead{font-size:11px}
  .venue-box .name{font-size:27px;line-height:1.02}

  .tagline{background:var(--yellow);font-size:7px;font-weight:700;padding:1px 3px;letter-spacing:.1px}

  .headline{font-family:"Alfa Slab One",serif;font-size:40px;color:var(--brown);letter-spacing:.5px;
    transform:translate(-50%,-50%) rotate(var(--a)) scaleX(.82)}
  .headline-rule{width:230px;height:2px;background:var(--ink)}

  .ticket{width:62px;height:52px;background:var(--white);border-radius:8px;text-align:center;
    box-shadow:1px 2px 3px rgba(0,0,0,.3);overflow:hidden;display:flex;flex-direction:column}
  .ticket .price{font-size:26px;font-weight:700;line-height:38px;flex:1}
  .ticket .label{background:var(--yellow);font-size:8px;font-weight:700;letter-spacing:2px;line-height:13px}

  .details{line-height:1.05}
  .details .time{font-size:20px;font-weight:500}
  .details .location{font-size:6.5px;color:var(--red-text);font-weight:500}
  .details .perks{font-size:14px;color:var(--red-text);font-weight:500}
  .details .info{font-size:10px}
  .details .web{font-size:10px;color:var(--red-text);font-weight:500}

  .beneficiary{position:absolute;left:392px;top:606px;display:flex;align-items:center;gap:5px;white-space:nowrap;
    font-weight:700;font-size:14px;color:var(--ink)}
  .beneficiary .mark{width:11px;height:11px;background:var(--ink)}
</style>
</head>
<body>
<div class="flyer-frame">
  <div class="flyer">
    <svg class="layer" viewBox="0 0 515 665" aria-hidden="true">
      <defs>
        <linearGradient id="goldFill" x1="0" y1="0" x2="1" y2="1">
          <stop offset="0" stop-color="var(--gold-light)"/>
          <stop offset="1" stop-color="var(--gold-dark)"/>
        </linearGradient>
      </defs>
      <path d="M336 252 Q326 262 336 272 L515 445 L515 40 Z" fill="url(#goldFill)"/>
      <g stroke="var(--stripe)" stroke-width="3">
        <line x1="420" y1="196" x2="515" y2="96"/>
        <line x1="432" y1="202" x2="515" y2="114"/>
        <line x1="444" y1="208" x2="515" y2="132"/>
      </g>
    </svg>

    <svg class="layer" viewBox="0 0 515 665" role="img" aria-label="Band performing on a blue-lit stage">
      <defs>
        <clipPath id="bandClip"><path d="M22 0 L372 0 L230 176 Q218 190 205 178 Z"/></clipPath>
        <linearGradient id="bandBase" x1="0" y1="0" x2="1" y2="1">
          <stop offset="0" stop-color="var(--band-dark)"/>
          <stop offset=".45" stop-color="var(--band-blue)"/>
          <stop offset="1" stop-color="var(--band-dark)"/>
        </linearGradient>
        <radialGradient id="bandLight"><stop offset="0" stop-color="var(--band-glow)" stop-opacity=".85"/><stop offset="1" stop-color="var(--band-glow)" stop-opacity="0"/></radialGradient>
        <radialGradient id="bandWarm"><stop offset="0" stop-color="var(--gold-light)" stop-opacity=".55"/><stop offset="1" stop-color="var(--gold-light)" stop-opacity="0"/></radialGradient>
      </defs>
      <g clip-path="url(#bandClip)">
        <rect width="515" height="200" fill="url(#bandBase)"/>
        <ellipse cx="180" cy="70" rx="90" ry="70" fill="url(#bandLight)"/>
        <ellipse cx="80" cy="40" rx="50" ry="40" fill="url(#bandLight)"/>
        <ellipse cx="310" cy="40" rx="60" ry="50" fill="url(#bandWarm)"/>
      </g>
    </svg>

    <svg class="layer" viewBox="0 0 515 665" role="img" aria-label="Drummer playing a kit, tinted red">
      <defs>
        <clipPath id="drumClip"><path d="M0 18 L285 314 Q296 328 285 342 L0 645 Z"/></clipPath>
        <linearGradient id="drumBase" x1="0" y1="0" x2="1" y2="0">
          <stop offset="0" stop-color="var(--drum-dark)"/>
          <stop offset=".75" stop-color="var(--drum-red)"/>
        </linearGradient>
        <radialGradient id="drumLight"><stop offset="0" stop-color="var(--drum-glow)" stop-opacity=".8"/><stop offset="1" stop-color="var(--drum-glow)" stop-opacity="0"/></radialGradient>
        <radialGradient id="drumShade"><stop offset="0" stop-color="var(--drum-dark)" stop-opacity=".7"/><stop offset="1" stop-color="var(--drum-dark)" stop-opacity="0"/></radialGradient>
      </defs>
      <g clip-path="url(#drumClip)">
        <rect width="300" height="665" fill="url(#drumBase)"/>
        <ellipse cx="140" cy="270" rx="110" ry="120" fill="url(#drumLight)"/>
        <ellipse cx="200" cy="380" rx="70" ry="50" fill="url(#drumLight)"/>
        <ellipse cx="90" cy="520" rx="100" ry="80" fill="url(#drumShade)"/>
      </g>
    </svg>

    <svg class="layer" viewBox="0 0 515 665" role="img" aria-label="Concert crowd under bright stage lights">
      <defs>
        <clipPath id="crowdClip"><path d="M66 665 L222 482 Q233 470 245 482 L416 665 Z"/></clipPath>
        <linearGradient id="crowdBase" x1="0" y1="0" x2="0" y2="1">
          <stop offset="0" stop-color="var(--crowd-mid)"/>
          <stop offset=".6" stop-color="var(--drum-dark)"/>
          <stop offset="1" stop-color="var(--crowd-dark)"/>
        </linearGradient>
        <radialGradient id="crowdLight"><stop offset="0" stop-color="var(--crowd-glow)" stop-opacity=".95"/><stop offset="1" stop-color="var(--crowd-glow)" stop-opacity="0"/></radialGradient>
      </defs>
      <g clip-path="url(#crowdClip)">
        <rect x="60" y="465" width="360" height="200" fill="url(#crowdBase)"/>
        <ellipse cx="230" cy="535" rx="70" ry="50" fill="url(#crowdLight)"/>
        <ellipse cx="180" cy="560" rx="40" ry="30" fill="url(#crowdLight)"/>
        <ellipse cx="290" cy="560" rx="40" ry="30" fill="url(#crowdLight)"/>
      </g>
    </svg>

    <div class="rot station" style="--x:412px;--y:72px;--a:-40deg"><span class="mark"></span>94.1 KVRL</div>

    <div class="rot event-name" style="--x:292px;--y:172px;--a:-38deg">
      <span class="mark"></span><span>Midwinter<br>Lantern Jubilee</span>
    </div>

    <div class="rot date-badge" style="--x:370px;--y:214px;--a:40deg">
      <span class="day">14</span><span class="month">JUN</span><span class="year">2018</span>
    </div>

    <div class="rot venue-box" style="--x:466px;--y:340px;--a:42deg">
      <div class="lead">LIVE FROM</div>
      <div class="name">LOREM<br>IPSUM</div>
    </div>

    <div class="rot tagline" style="--x:425px;--y:390px;--a:42deg">LOREM IPSUM DOLOR SIT AMET, VIDIT POSSE PERTINAX VIM AD</div>

    <div class="rot headline" style="--x:403px;--y:418px;--a:42deg">LIVE MUSIC</div>
    <div class="rot headline-rule" style="--x:390px;--y:436px;--a:42deg"></div>

    <div class="rot ticket" style="--x:294px;--y:430px;--a:42deg">
      <span class="price">$20</span><span class="label">TICKETS</span>
    </div>

    <div class="rot details" style="--x:378px;--y:505px;--a:42deg">
      <div class="time">TIME-5.00PM</div>
      <div class="location">LOCATION-228 LINDEN AVE. RIVERTON</div>
      <div class="perks">FREE DRINKS &amp; FOOD</div>
      <div class="info">FOR MORE INFORMATION VISIT-</div>
      <div class="web">WWW.WEBSITE.COM</div>
    </div>

    <div class="beneficiary"><span class="mark"></span>Mesa Street Care</div>
  </div>
</div>
</body>
</html>
```